velmora - business cards

Need business card designs - logo provided - see www.velmora-example.co.nz

Industry/Entity Type

Business

Requirements
Must have
• logo - provided in attachments
• www.velmora-example.co.nz

```html
<!DOCTYPE html>
<html lang="en">
<head>
<meta charset="utf-8">
<title>velmora – business cards</title>
<link href="https://fonts.googleapis.com/css2?family=Arimo:wght@400;700&display=swap" rel="stylesheet">
<style>
  :root {
    --bg: #e9e9e9;
    --brand-blue: #1a78bf;
    --brand-blue-deep: #0f5fa3;
    --card-white: #f1f1f1;
    --ink: #3f3f41;
    --ink-soft: #555558;
    --accent-orange: #e0771e;
    --text-font: "Arimo", Arial, sans-serif;
  }
  * { box-sizing: border-box; margin: 0; padding: 0; }
  html, body { width: 1200px; height: 900px; overflow: hidden; }
  body {
    background: var(--bg);
    font-family: var(--text-font);
    display: flex;
    flex-direction: column;
    align-items: center;
    justify-content: center;
    gap: 56px;
  }
  .card {
    width: 640px;
    height: 366px;
    position: relative;
    box-shadow: 0 2px 8px rgba(0,0,0,0.12);
  }
  .wordmark {
    display: flex;
    align-items: center;
    gap: 18px;
    font-family: var(--text-font);
    font-weight: 700;
    letter-spacing: -1px;
    line-height: 1;
  }
  .wordmark-dot {
    border-radius: 50%;
    flex: none;
  }

  /* Front */
  .card-front {
    background: radial-gradient(ellipse at 55% 40%, var(--brand-blue) 0%, var(--brand-blue-deep) 100%);
    display: flex;
    align-items: center;
    justify-content: center;
  }
  .card-front .wordmark { font-size: 78px; color: var(--ink); }
  .card-front .wordmark-dot { width: 62px; height: 62px; background: #ffffff; }

  /* Back */
  .card-back { background: var(--card-white); color: var(--ink); }
  .card-back .wordmark {
    position: absolute; left: 44px; top: 70px;
    font-size: 62px; color: var(--ink);
  }
  .card-back .wordmark-dot { width: 50px; height: 50px; background: var(--brand-blue); }
  .holder {
    position: absolute; left: 44px; top: 160px;
    display: flex; align-items: baseline; gap: 8px;
  }
  .holder-name { font-size: 24px; color: var(--ink); }
  .holder-role { font-size: 13px; text-transform: uppercase; color: var(--ink-soft); }
  .contact-list {
    position: absolute; left: 44px; top: 204px;
    list-style: none; font-size: 14px; line-height: 1.55; color: var(--ink);
  }
  .contact-list li { display: flex; align-items: center; gap: 8px; }
  .contact-list li::before {
    content: ""; width: 0; height: 0;
    border-left: 7px solid var(--accent-orange);
    border-top: 4.5px solid transparent;
    border-bottom: 4.5px solid transparent;
  }
  .contact-label { font-weight: 700; }
  .address-block {
    position: absolute; right: 40px; top: 62px;
    text-align: right; font-size: 13px; line-height: 1.35; color: var(--ink);
  }
  .address-rule {
    height: 1.5px; background: var(--accent-orange);
    margin: 6px 0 6px auto; width: 100%;
  }
  .web-name { color: var(--accent-orange); font-weight: 700; }
</style>
</head>
<body>
  <section class="card card-front" aria-label="Business card front">
    <div class="wordmark"><span class="wordmark-dot"></span>velmora</div>
  </section>

  <section class="card card-back" aria-label="Business card back">
    <div class="wordmark"><span class="wordmark-dot"></span>velmora</div>
    <div class="holder">
      <span class="holder-name">Marissa Coleby</span>
      <span class="holder-role">Operation Manager</span>
    </div>
    <ul class="contact-list">
      <li><span><span class="contact-label">International:</span> +64 21 000 482</span></li>
      <li><span><span class="contact-label">Phone NZ:</span> 0800 2 VELMO (0800 83-56-66)</span></li>
      <li><span><span class="contact-label">Email:</span> info@velmora-example.co.nz</span></li>
    </ul>
    <address class="address-block" style="font-style:normal">
      P.O.Box 400218,<br>
      Hillcrest, 0999,<br>
      New Zealand
      <div class="address-rule"></div>
      www.<span class="web-name">velmora</span>-example.co.nz
    </address>
  </section>
</body>
</html>
```